Webdesign für Naturheilpraktiker gesucht
Zielgruppe
Ich arbeite im Gesundheitswesen als Naturheilpraktiker Traditionell Tibetische Medizin.
Verfüge aber über verschiedene Anwendungstechniken.
Die Zielgruppe sind alle Menschen die mehr als nur klassische Medizin wollen, die mit der klassischen Schulmedizin nicht mehr weiter kommen und einen alternativen Weg suchen. Menschen die neben der Schulmedizin noch einen anderen Weg suchen.
Menschen im Wellness und Fitnessbereich.
Ernährungsbewusste Menschen.
Sportler allgemein da ich über eine neue Technik verfüge (KERVO) die erst auf den Markt kommt und mit der verschiedene Beschwerden gelindert werden können.
Grob gesagt alles was mit Medizin, Komplementärmedizin, Gesundheit, Wellness, Sport usw zu tun hat.
Kompetenzen der Traditionell Tibetische Medizin:
- Massage als Gesundheitssystem oder als Wellness
- Ernährungsberatung
- tibetisches Yoga
- Lebensberatung
- Familienstellen
Aufgabenstellung
Der Firmennamen und das Logo bestehen.
In der Tradition der tibetischen Medizin ist vor allem Blau (Medizin Buddha) die Farben sind aber frei wählbar.
Es soll Vertrautheit, Geborgenheit und Wärme ausstrahlen.
Nicht zu feminin erscheinen.
Einfach ein paar Ideen
http://massagepraxis-wolfrin.example
http://www.himalheilkunde.example

```html
<!DOCTYPE html>
<html lang="de">
<head>
<meta charset="utf-8">
<title>Tibetische Massage – ATMAVITA</title>
<link rel="stylesheet" href="https://fonts.googleapis.com/css2?family=Open+Sans:wght@400;600;700&family=Josefin+Sans:wght@400;600&family=Quicksand:wght@400&display=swap">
<style>
  :root{
    --ink:#3d3d3d;
    --text:#555a60;
    --navy:#1f4f8f;
    --teal:#2fb58f;
    --nav:#7a4a2a;
    --band:#ebebf0;
    --footer:#4a4a4a;
    --white:#ffffff;
    --muted:#6e6e6e;
  }
  *{box-sizing:border-box;margin:0;padding:0}
  html,body{width:1200px;height:1150px;overflow:hidden}
  body{position:relative;background:var(--white);font-family:"Open Sans",Arial,sans-serif;color:var(--text)}

  .hero{position:absolute;left:0;top:0;width:1200px;height:246px;
    background:linear-gradient(100deg,#fbe3c9 0%,#fbe6cf 35%,#f7d6b8 60%,#e9a887 78%,#f3d0b4 100%)}
  .brand{position:absolute;left:235px;top:72px;display:flex;align-items:center;gap:8px}
  .brand-dot{width:16px;height:16px;border-radius:50%;background:var(--navy)}
  .brand-name{font-family:"Open Sans",Arial,sans-serif;font-weight:700;font-size:13px;letter-spacing:3px;color:var(--navy)}
  .brand-tag{position:absolute;left:235px;top:94px;font-size:4px;letter-spacing:.3px;color:var(--navy)}
  .nav{position:absolute;right:235px;top:49px;display:flex;align-items:center;gap:9px;
    font-family:"Josefin Sans",Arial,sans-serif;font-size:7.2px;letter-spacing:.4px;color:var(--nav)}
  .nav .sep{width:2px;height:2px;border-radius:50%;background:#e6b48c}
  .hero-title{position:absolute;left:0;width:1200px;top:156px;text-align:center;
    font-weight:600;font-size:27px;color:var(--ink)}
  .divider{position:absolute;left:563px;top:197px}

  .intro-photo{position:absolute;left:235px;top:290px;width:223px;height:115px;
    background:linear-gradient(120deg,#8a5a3f 0%,#d9a585 35%,#efe6d8 60%,#c48a66 100%)}
  .copy{font-size:7.8px;line-height:12.6px}
  .copy p+p{margin-top:12.6px}
  .intro-text{position:absolute;left:488px;top:284px;width:480px}
  .detail-text{position:absolute;left:235px;top:450px;width:345px}

  .checklist{position:absolute;left:620px;top:434px;list-style:none;
    font-family:"Quicksand",Arial,sans-serif;font-size:11px;color:var(--navy)}
  .checklist li{display:flex;align-items:center;height:24px}
  .checklist li.wide{margin-top:11px}
  .checklist svg{margin-right:11px}

  .band{position:absolute;left:0;top:675px;width:1200px;height:255px;background:var(--band)}
  .band-mark{position:absolute;left:268px;top:80px;width:155px;height:155px;display:flex;flex-direction:column;
    align-items:center;justify-content:center;gap:8px}
  .band-mark .ring{width:28px;height:28px;border-radius:50%;background:var(--navy)}
  .band-mark .name{font-weight:700;font-size:14px;letter-spacing:3px;color:var(--navy)}
  .band-text{position:absolute;left:488px;top:76px;width:480px}
  .band-text h3{font-size:7.8px;font-weight:700;color:var(--ink);margin-bottom:12px}
  .button{position:absolute;left:488px;top:170px;width:141px;height:24px;border-radius:12px;background:var(--navy);
    color:var(--white);font-size:7.2px;display:flex;align-items:center;justify-content:center;gap:4px}

  .footer{position:absolute;left:0;top:930px;width:1200px;height:220px;background:var(--footer)}
  .footer-brand{position:absolute;left:0;width:1200px;top:45px;display:flex;justify-content:center;align-items:center;gap:8px}
  .footer-brand .dot{width:14px;height:14px;border-radius:50%;background:#c9c9c9}
  .footer-brand .name{font-weight:700;font-size:13px;letter-spacing:3px;color:#c9c9c9}
  .social{position:absolute;left:509px;top:123px;display:flex;gap:8px}
  .social span{width:30px;height:30px;border-radius:50%;background:var(--white)}
  .copyright{position:absolute;left:0;width:1200px;top:181px;text-align:center;font-size:7.8px;color:var(--muted)}
  .to-top{position:absolute;left:1157px;top:167px;width:30px;height:30px;border:1px solid var(--white);
    display:flex;align-items:center;justify-content:center}
</style>
</head>
<body>
  <header class="hero" role="img" aria-label="Unscharfes Foto: Hand mit Löffel über einer Massageliege mit rotem Tuch, warme Pfirsichtöne">
    <div class="brand"><span class="brand-dot"></span><span class="brand-name">ATMAVITA</span></div>
    <div class="brand-tag">NATURHEILPRAXIS TRADITIONELL TIBETISCHE MEDIZIN</div>
    <nav class="nav">
      <span>HOME</span><span class="sep"></span>
      <span>ÜBER MICH</span><span class="sep"></span>
      <span>TIBETISCHE MEDIZIN</span><span class="sep"></span>
      <span>ANGEBOT</span><span class="sep"></span>
      <span>TERMINE</span><span class="sep"></span>
      <span>KONTAKT</span>
    </nav>
    <h1 class="hero-title">Tibetische Massage</h1>
    <svg class="divider" width="74" height="16" viewBox="0 0 74 16">
      <line x1="0" y1="8" x2="23" y2="8" stroke="#2fb58f" stroke-width="1.2"/>
      <line x1="51" y1="8" x2="74" y2="8" stroke="#2fb58f" stroke-width="1.2"/>
      <circle cx="37" cy="8" r="6" fill="none" stroke="#2fb58f" stroke-width="1.2"/>
    </svg>
  </header>

  <div class="intro-photo" role="img" aria-label="Foto: Rückenmassage mit warmen Steinen auf weißem Tuch"></div>
  <div class="intro-text copy">
    <p>Die tibetische Massage hat seine Wurzeln schon in der Lehre Buddhas Shakyamuni.</p>
    <p>Der Mensch wird als Ganzheit von Körper, Geist und Seele erfasst und Behandelt.</p>
    <p>Nicht nur dem Körper sondern auch der Psyche oder dem Geist kommt besondere Bedeutung bei der Behandlung zu.<br>Die Massage eignet sich vor allem für psychosomatische Beschwerden.</p>
    <p>Die Grundlagen der Tibetischen Medizin bilden die drei Körperenergien Lung (Wind) – Tripa (Feuer) – Badkan (Schleim) die für die Körperfunktion und auch den Geisteszustand verantwortlich sind.<br>Sind alle drei Energien im Gleichgewicht erfreuen wir uns bester Gesundheit.</p>
  </div>

  <div class="detail-text copy">
    <p>In der Tibetischen Massage ist es das Ziel die drei Energien auszugleichen und somit das Gleichgewicht herzustellen. Die tibetische Massage ist eine ganzheitliche, tief wirkende Massage die die innere Stabilität und den Heilprozess fördert.</p>
    <p>Sie eignet sich daher sehr gut zur Unterstützung anderer Therapien und oder zur Entspannung.</p>
    <p>Es ist eine je nach Symptomen sanfte oder kräftige Ölmassage die unter anderem Verspannungen und Energieblockaden löst und das physische und psychische Wohlbefinden fördert.</p>
  </div>

  <ul class="checklist">
    <li><svg width="9" height="9" viewBox="0 0 9 9"><path d="M1 5 L3.5 8 L8 1" fill="none" stroke="#1f4f8f" stroke-width="1.6"/></svg>Verspannungen</li>
    <li><svg width="9" height="9" viewBox="0 0 9 9"><path d="M1 5 L3.5 8 L8 1" fill="none" stroke="#1f4f8f" stroke-width="1.6"/></svg>Schlafstörungen</li>
    <li><svg width="9" height="9" viewBox="0 0 9 9"><path d="M1 5 L3.5 8 L8 1" fill="none" stroke="#1f4f8f" stroke-width="1.6"/></svg>Nervosität</li>
    <li><svg width="9" height="9" viewBox="0 0 9 9"><path d="M1 5 L3.5 8 L8 1" fill="none" stroke="#1f4f8f" stroke-width="1.6"/></svg>Unruhe</li>
    <li><svg width="9" height="9" viewBox="0 0 9 9"><path d="M1 5 L3.5 8 L8 1" fill="none" stroke="#1f4f8f" stroke-width="1.6"/></svg>Stress</li>
    <li><svg width="9" height="9" viewBox="0 0 9 9"><path d="M1 5 L3.5 8 L8 1" fill="none" stroke="#1f4f8f" stroke-width="1.6"/></svg>Verwirrtheit</li>
    <li><svg width="9" height="9" viewBox="0 0 9 9"><path d="M1 5 L3.5 8 L8 1" fill="none" stroke="#1f4f8f" stroke-width="1.6"/></svg>Konzentrationsschwäche</li>
    <li class="wide"><svg width="9" height="9" viewBox="0 0 9 9"><path d="M1 5 L3.5 8 L8 1" fill="none" stroke="#1f4f8f" stroke-width="1.6"/></svg>Energielosigkeit und zur Entspannung im Allgemeinen (Wellness)</li>
  </ul>

  <section class="band">
    <div class="band-mark"><span class="ring"></span><span class="name">ATMAVITA</span></div>
    <div class="band-text copy">
      <h3>Muster Text Lorem ipsum dolor sit amet consetetur.</h3>
      <p>Lorem ipsum dolor sit amet, consetetur sadipscing elitr, sed diam nonumy eirmod tempor invidunt ut labore.<br>Et dolore magna aliquyam erat, sed diam voluptua. At vero eos et accusam et justo duo dolores et ea rebum Stet clita kasd gubergren, no sea takimata sanctus est Lorem ipsum dolor sit amet. Lorem ipsum dolor sit amet, consetetur sadipscing elitr, sed diam nonumy eirmod tempor invidunt ut labore.</p>
    </div>
    <div class="button">
      <svg width="8" height="7" viewBox="0 0 8 7"><path d="M1 6 C1 3 3 2 5 2 L5 0.5 L7.5 3 L5 5.5 L5 4 C3 4 2 4.5 1 6 Z" fill="none" stroke="#fff" stroke-width="0.8"/></svg>
      JETZT KONTAKT AUFNEHMEN
    </div>
  </section>

  <footer class="footer">
    <div class="footer-brand"><span class="dot"></span><span class="name">ATMAVITA</span></div>
    <div class="social"><span></span><span></span><span></span><span></span><span></span></div>
    <p class="copyright">© 2018 ATMAVITA. Alle Rechte vorbehalten</p>
    <div class="to-top"><svg width="8" height="5" viewBox="0 0 8 5"><path d="M1 4.5 L4 1.5 L7 4.5" fill="none" stroke="#fff" stroke-width="1.2"/></svg></div>
  </footer>
</body>
</html>
```